KVR PROTECTIVE COATINGS BROCHURE

To design a 4 page A4 brochure of protective coating system for steel and concrete infrastructure with industrial , telecoms and oil & gas markets.

brochure title; Inorganic siloxane protective coatings for steel and concrete infrastructure
sub title - Non-isocyanate (NISO) Coatings
Products:
- KVR 100 1K solvent free inorganic tintable finish coat for ultra UV durability
- KVR 100 CC 1K solvent free clear coat for protection of steel and concrete substrates, anti graffiti, highly UV resistant
- KVR PRIMER 2K epoxy hybrid anti corrosion coating for steel
- KVR CERAMIC 1K glass flake single pack high abrasion resistant coating
- KVR DURAMETAL 1K single component siloxane zinc anti-corrosion coating
- KVR TEL 1K single component intermediate anti-corrosion coating
- KVR 220 2K two component epoxy-siloxane hybrid durable tintable top coat
- KVR GROUNDSEAL 2K two component, chemical resistant, durable floor coating.
- KVR SHARDLAYER 2K two component ceramically filled epoxy for high abrasion resistance.

use good clear images of markets sectors (oil&gas, Telecoms, Industrial)
use icons for low VOC, low toxicity, Green, high weathering resistance, chemical resistance, maintenance friendly, environment friendly, non-isocyanate.

Table of primers and top coats in attachment, please use images within document about tinting products

Company Info
Tel +44 (0) 1632 960518
Email sales@tq-nx.example
Address 7-8 Wexcombe Lea Trading Estate, Candle Lane, United Kingdom
web www.tq-nx.example

Target Market(s)

Protective Coatings

Requirements
Must have
• Clear images of target markets and good layout of information provided

```html
<!DOCTYPE html>
<html lang="en">
<head>
<meta charset="utf-8">
<title>KVR Protective Coatings Brochure</title>
<link href="https://fonts.googleapis.com/css2?family=Montserrat:wght@300;400;600;700;800&display=swap" rel="stylesheet">
<style>
:root{
  --navy:#1c3f94;
  --blue:#2f6fc6;
  --sky:#3b8fd9;
  --light:#eef1f5;
  --ink:#2b2f3a;
  --white:#ffffff;
  --bg:#e4e6ea;
}
*{box-sizing:border-box;margin:0;padding:0}
html,body{width:720px;height:1200px;overflow:hidden;background:var(--bg);font-family:'Montserrat',sans-serif;color:var(--ink)}
.canvas{position:relative;width:720px;height:1200px}
.spread{position:absolute;left:20px;width:680px;height:481px;display:flex;box-shadow:0 6px 18px rgba(0,0,0,.18)}
.spread--covers{top:99px}
.spread--inner{top:620px}
.page{position:relative;width:340px;height:481px;overflow:hidden;background:var(--white)}
.photo{position:absolute}
.frame{border:4px solid var(--white);box-shadow:0 2px 8px rgba(0,0,0,.2)}

/* front cover */
.front{background:linear-gradient(180deg,#f4f5f7 0,#fff 40%,#f1f2f4 100%)}
.brand{position:absolute;display:flex;align-items:center;gap:6px;font-weight:700;color:var(--navy)}
.brand__dot{width:12px;height:12px;border-radius:50%;background:var(--sky)}
.front .brand{left:118px;top:20px;font-size:14px}
.front__refinery{left:40px;top:58px;width:300px;height:205px;background:linear-gradient(170deg,#e9c6dc 0%,#b592c4 35%,#5a5f93 65%,#1f2c55 100%)}
.front__telecom{left:12px;top:196px;width:94px;height:170px;background:linear-gradient(180deg,#9cc3e6 0%,#3c7fbf 55%,#1b3d6e 100%)}
.cover-title{position:absolute;right:18px;top:284px;text-align:right;font-size:12px;line-height:1.2;font-weight:400}
.cover-title span{display:block}
.cover-title__l1{font-size:18px;font-weight:800;color:var(--navy)}
.cover-title__l2{font-size:15px;font-weight:800;color:var(--sky)}
.cover-title__l3{font-size:12.5px;font-weight:300;color:var(--ink);letter-spacing:.3px}
.cover-title__l4{font-size:12.5px;font-weight:400;color:var(--ink);letter-spacing:.3px;margin-right:10px}
.cover-sub{position:absolute;right:18px;top:376px;font-size:11.5px;font-weight:800;color:var(--navy)}
.cover-web{position:absolute;right:60px;top:428px;font-size:9px;font-weight:600;letter-spacing:2.5px;color:var(--navy)}

/* back cover */
.back{background:linear-gradient(180deg,#2e63c0 0%,#3a78d0 50%,#4f8ad8 100%)}
.back__tanks{left:0;top:0;width:340px;height:150px;background:linear-gradient(180deg,#2c5fb8 0%,#5d93dc 100%);opacity:.9}
.back__rig{left:0;top:158px;width:340px;height:170px;background:linear-gradient(180deg,#7eb0e6 0%,#a9c6e4 45%,#2f5fa8 75%,#1e4a8f 100%)}
.back__person{left:210px;top:330px;width:130px;height:150px;background:linear-gradient(180deg,#5f91d6,#3f74c6)}
.contact{position:absolute;left:36px;top:286px;width:214px;background:var(--white);padding:10px 12px;text-align:center;outline:1px solid rgba(255,255,255,.8);outline-offset:6px}
.contact__head{font-size:8.5px;font-weight:700;color:var(--navy);margin-bottom:1px}
.contact__text{font-size:6.6px;line-height:1.35;color:var(--ink)}
.contact__tel{font-size:6.6px;line-height:1.4;color:var(--sky)}
.contact__tel b{color:var(--navy);font-weight:700;font-size:7.5px}
.contact__block{margin-bottom:7px}
.contact__web{font-size:9px;color:var(--navy);letter-spacing:.5px}

/* inner left */
.inner-left{background:#f7f8fa}
.icon-band{position:absolute;left:0;top:0;width:340px;height:150px;background:linear-gradient(180deg,#2e63c0,#3f7dd2)}
.icons{position:absolute;left:12px;top:14px;display:flex;gap:9px}
.icon{width:38px;height:38px;border:1.5px solid var(--white);border-radius:50%;display:flex;flex-direction:column;align-items:center;justify-content:center;color:var(--white);font-size:4.5px;font-weight:700;text-align:center;line-height:1.1}
.icon svg{width:16px;height:16px}
.inner-left__plant{left:10px;top:64px;width:210px;height:150px;background:linear-gradient(180deg,#a7c7ea 0%,#8aa0b8 45%,#3e5470 100%)}
.inner-left__refinery{left:196px;top:150px;width:144px;height:180px;background:linear-gradient(180deg,#c9d8ea 0%,#8e9aa9 50%,#4a5564 100%)}
.inner-left__tablet{left:196px;top:340px;width:144px;height:88px;background:linear-gradient(135deg,#1f3f7a 0%,#3d78c8 60%,#9cc1e8 100%)}
.products{position:absolute;left:16px;top:226px;width:176px}
.products__title{font-size:10px;font-weight:800;color:var(--navy);margin-bottom:4px}
.products__list{list-style:none}
.products__list li{font-size:6.6px;line-height:1.3;margin-bottom:3.5px;padding-left:6px;position:relative}
.products__list li::before{content:"·";position:absolute;left:0;color:var(--navy);font-weight:800}
.products__list b{color:var(--navy);font-weight:800;font-size:7.4px}

/* inner right */
.inner-right__house{left:0;top:0;width:180px;height:95px;background:linear-gradient(180deg,#e9eef3 0%,#c7a48f 60%,#7c8a5c 100%)}
.inner-right__roof{left:150px;top:0;width:190px;height:70px;background:linear-gradient(180deg,#eef1f4,#c8ced6)}
.table-title{position:absolute;left:20px;font-size:8.5px;font-weight:800;color:var(--navy)}
.table-title span{color:var(--sky)}
.spec{position:absolute;left:20px;width:304px;border-collapse:collapse;font-size:5.6px;line-height:1.2}
.spec th,.spec td{border:0.5px solid #555;padding:1px 3px;text-align:center}
.spec th{font-weight:700}
.spec td:first-child,.spec th:first-child{text-align:left}
.inner-right__machine{left:20px;top:306px;width:150px;height:160px;background:linear-gradient(180deg,#c9cdd2 0%,#9ea4ab 55%,#6f757c 100%)}
.inner-right__chart{left:184px;top:336px;width:142px;height:90px;background:linear-gradient(90deg,#c43a3a,#e8a23b,#e6d84a,#5aa55a,#3a7ec4,#7a4fa6,#8b6a52,#999)}
</style>
</head>
<body>
<div class="canvas">

  <section class="spread spread--covers">
    <article class="page back">
      <div class="photo back__tanks" role="img" aria-label="Faint photo of spherical gas storage tanks"></div>
      <div class="photo back__rig" role="img" aria-label="Photo of an offshore oil and gas platform with flare stack at sea"></div>
      <div class="photo back__person" role="img" aria-label="Faint photo of a customer service agent with headset"></div>
      <div class="contact">
        <div class="contact__block">
          <p class="contact__head">Head Office</p>
          <p class="contact__text">Kelvara Resins Ltd<br>7-8 Wexcombe Lea Trading Estate,<br>Candle Lane, United Kingdom</p>
          <p class="contact__tel">Telephone: <b>+44 (0) 1632 960518</b></p>
          <p class="contact__tel">Email: <b>sales@tq-nx.example</b></p>
        </div>
        <div class="contact__block">
          <p class="contact__head">American Office</p>
          <p class="contact__text">Kelvara Resins Americas LLC<br>480 Larkspur Bend Cedar Hollow, TX<br>77000, USA</p>
          <p class="contact__tel">Telephone: <b>+1 555 010 4721</b></p>
        </div>
        <p class="contact__web">WWW.TQ-NX.EXAMPLE</p>
      </div>
    </article>

    <article class="page front">
      <div class="brand"><span class="brand__dot"></span>Kelvara Resins</div>
      <div class="photo front__refinery" role="img" aria-label="Photo of an oil refinery at dusk under a pink sky"></div>
      <div class="photo frame front__telecom" role="img" aria-label="Photo of a telecom mast with network graphics"></div>
      <h1 class="cover-title">
        <span class="cover-title__l1">INORGANIC SILOXANE</span>
        <span class="cover-title__l2">PROTECTIVE COATINGS</span>
        <span class="cover-title__l3">FOR STEEL AND CONCRETE</span>
        <span class="cover-title__l4">INFRASTRUCTURE</span>
      </h1>
      <p class="cover-sub">NON-ISOCYANATE (NISO) COATINGS</p>
      <p class="cover-web">WWW.TQ-NX.EXAMPLE</p>
    </article>
  </section>

  <section class="spread spread--inner">
    <article class="page inner-left">
      <div class="icon-band"></div>
      <div class="icons">
        <div class="icon"><svg viewBox="0 0 24 24" fill="none" stroke="#fff" stroke-width="1.6"><path d="M12 20V11M12 11c0-4 3-6 7-6 0 4-3 6-7 6zM12 14c0-3-2-5-6-5 0 3 2 5 6 5z"/></svg>LOW VOC</div>
        <div class="icon"><svg viewBox="0 0 24 24" fill="none" stroke="#fff" stroke-width="1.6"><path d="M12 3l8 4v5c0 5-4 8-8 9-4-1-8-4-8-9V7z"/></svg>LOW TOX</div>
        <div class="icon"><svg viewBox="0 0 24 24" fill="none" stroke="#fff" stroke-width="1.6"><circle cx="12" cy="12" r="4"/><path d="M12 2v4M12 18v4M2 12h4M18 12h4"/></svg>WEATHER</div>
        <div class="icon"><svg viewBox="0 0 24 24" fill="none" stroke="#fff" stroke-width="1.6"><path d="M9 3h6M10 3v6l-5 10h14l-5-10V3"/></svg>CHEMICAL RESISTANT</div>
        <div class="icon"><svg viewBox="0 0 24 24" fill="none" stroke="#fff" stroke-width="1.6"><circle cx="12" cy="12" r="3"/><path d="M12 4v3M12 17v3M4 12h3M17 12h3"/></svg>MAINTAIN</div>
        <div class="icon"><svg viewBox="0 0 24 24" fill="none" stroke="#fff" stroke-width="1.6"><path d="M4 18h16M12 18V9M12 9c0-3 2-5 5-5 0 3-2 5-5 5z"/></svg>GREEN</div>
        <div class="icon"><svg viewBox="0 0 24 24" fill="none" stroke="#fff" stroke-width="1.6"><circle cx="12" cy="12" r="8"/><path d="M6 6l12 12"/></svg>NISO</div>
      </div>
      <div class="photo inner-left__plant" role="img" aria-label="Photo of an industrial process plant with pipework"></div>
      <div class="photo frame inner-left__refinery" role="img" aria-label="Photo of refinery distillation columns"></div>
      <div class="photo frame inner-left__tablet" role="img" aria-label="Photo of a hand touching an innovation concept interface"></div>
      <div class="products">
        <h2 class="products__title">PRODUCTS:</h2>
        <ul class="products__list">
          <li><b>KVR 100 1K</b> solvent free inorganic tintable finish coat for ultra UV durability</li>
          <li><b>KVR 100 CC 1K</b> solvent free clear coat for protection of steel and concrete substrates, anti graffiti, highly UV resistant</li>
          <li><b>KVR PRIMER 2K</b> epoxy hybrid anti corrosion coating for steel</li>
          <li><b>KVR CERAMIC 1K</b> glass flake single pack high abrasion resistant coating</li>
          <li><b>KVR DURAMETAL 1K</b> single component siloxane zinc anti-corrosion coating</li>
          <li><b>KVR TEL 1K</b> single component intermediate anti-corrosion coating</li>
          <li><b>KVR 220 2K</b> two component epoxy-siloxane hybrid durable tintable top coat</li>
          <li><b>KVR GROUNDSEAL 2K</b> two component, chemical resistant, durable floor coating.</li>
          <li><b>KVR SHARDLAYER 2K</b> two component ceramically filled epoxy for high abrasion resistance.</li>
        </ul>
      </div>
    </article>

    <article class="page inner-right">
      <div class="photo inner-right__roof" role="img" aria-label="Photo of an industrial roof with coated surfaces"></div>
      <div class="photo frame inner-right__house" role="img" aria-label="Photo of a thermal camera inspecting a house"></div>
      <h3 class="table-title" style="top:106px">1 AND 2 COMPONENT SILOXANE <span>BASED COATINGS:</span></h3>
      <table class="spec" style="top:120px">
        <tr><th>Product</th><th>Components</th><th>Functionality</th><th>Chemistry</th><th>DFT (µm)</th></tr>
        <tr><td>KVR TEL 1K</td><td>1</td><td>Anti-corrosion Primer</td><td>Siloxane</td><td>150 - 200</td></tr>
        <tr><td>KVR DURAMETAL 1K</td><td>1</td><td>Anti-corrosion Primer</td><td>Siloxane-Zinc</td><td>75-100</td></tr>
        <tr><td>KVR CERAMIC 1K</td><td>1</td><td>Abrasion resistant Primer</td><td>Siloxane-Ceramic</td><td>200-250</td></tr>
        <tr><td>KVR 100 1K</td><td>1</td><td>Durable Topcoat</td><td>Siloxane</td><td>75-150</td></tr>
        <tr><td>KVR 100 CC 1K</td><td>1</td><td>Durable clear coat (anti-graffiti)</td><td>Siloxane</td><td>25-50</td></tr>
        <tr><td>KVR PRIMER 2K</td><td>2</td><td>Anti-corrosion Primer</td><td>Epoxy-Hybrid</td><td>100 - 200</td></tr>
        <tr><td>KVR SHARDLAYER 2K</td><td>2</td><td>Abrasion resistant Primer</td><td>Epoxy-Ceramic</td><td>200-250</td></tr>
        <tr><td>KVR 220 2K</td><td>2</td><td>Durable Topcoat</td><td>Siloxane-Hybrid</td><td>75-150</td></tr>
        <tr><td>KVR GROUNDSEAL 2K</td><td>2</td><td>UV durable floor coating</td><td>Siloxane-hybrid</td><td>200-250</td></tr>
      </table>
      <h3 class="table-title" style="top:232px">TINTABLE TOP <span>COATS:</span></h3>
      <table class="spec" style="top:246px">
        <tr><th>Product</th><th>Components</th><th>Functionality</th><th>Tintable Colours</th><th>DFT (µm)</th></tr>
        <tr><td>KVR 100 1K</td><td>1</td><td>Durable Topcoat</td><td>RAL, BS &amp; Custom</td><td>75-150</td></tr>
        <tr><td>KVR 220 2K</td><td>2</td><td>Durable Topcoat</td><td>RAL, BS &amp; Custom</td><td>75-150</td></tr>
        <tr><td>KVR GROUNDSEAL 2K</td><td>2</td><td>UV durable floor coating</td><td>RAL, BS &amp; Custom</td><td>200-250</td></tr>
      </table>
      <div class="photo inner-right__machine" role="img" aria-label="Photo of an automatic tinting machine with a coating tin"></div>
      <div class="photo inner-right__chart" role="img" aria-label="RAL colour swatch chart"></div>
    </article>
  </section>

</div>
</body>
</html>
```